Website design for an Italian restaurant in Amsterdam

I need a design for a client of mine. It is for Teatro Lucerna, an Italian restaurant in Amsterdam.
We are going for a clean, modern look but we also need to realise an authentic feel.
The restaurant is located in an old movie theatre, that is where the name Teatro Lucerna comes from.
Industry/Entity Type
Italian Restaurant
Number of Pages Required
1 page
Font styles to use
Sans Serif
Colors
Designer to choose colors to be used in the design.

```html
<!DOCTYPE html>
<html lang="en">
<head>
<meta charset="utf-8">
<title>Teatro Lucerna – Italian Restaurant</title>
<link rel="stylesheet" href="https://fonts.googleapis.com/css2?family=Open+Sans:ital,wght@0,300;0,400;0,600;0,700;1,400&display=swap">
<style>
:root{
  --red:#c0201f;
  --red-dark:#a81a1a;
  --ink:#1f1f1f;
  --text:#444;
  --muted:#777;
  --light:#f6f6f6;
  --footer:#242424;
  --white:#fff;
}
*{margin:0;padding:0;box-sizing:border-box}
html,body{width:1200px;height:3727px;overflow:hidden;background:var(--white)}
body{position:relative;font-family:"Open Sans",sans-serif;color:var(--text)}
.abs{position:absolute}
.photo{position:absolute}

/* hero */
.hero{position:absolute;left:0;top:0;width:1200px;height:621px;
  background:radial-gradient(ellipse at 55% 70%,#c9a98a 0%,#7b6a5a 35%,#3b332d 70%,#1f1b18 100%)}
.hero-shade{position:absolute;inset:0;background:rgba(0,0,0,.28)}
.topbar{position:absolute;left:0;top:0;width:1200px;height:95px;background:rgba(10,10,10,.55)}
.brand{position:absolute;left:150px;top:30px;width:150px;text-align:center;color:var(--white)}
.brand-name{font-size:13px;font-weight:600;letter-spacing:.5px;border-bottom:1px solid var(--white);padding-bottom:5px}
.brand-sub{font-size:10px;margin-top:5px}
.nav{position:absolute;left:410px;top:38px;display:flex;font-size:15px;color:var(--white)}
.nav a{color:var(--white);text-decoration:none;padding:0 14px;border-left:1px solid rgba(255,255,255,.7);line-height:14px}
.nav a:first-child{border-left:none;text-decoration:underline}
.btn-book{position:absolute;left:919px;top:27px;width:154px;height:45px;border:1px solid var(--white);
  color:var(--white);font-size:15px;display:flex;align-items:center;justify-content:center}
.hero-title{position:absolute;left:0;width:1200px;text-align:center;color:var(--white);font-weight:700;text-shadow:0 2px 6px rgba(0,0,0,.5)}
.hero-title.small{top:252px;font-size:38px}
.hero-title.big{top:304px;font-size:52px}
.hero-info{position:absolute;left:0;width:1200px;text-align:center;color:var(--white);font-size:16px;font-weight:600;display:flex;justify-content:center;align-items:center;gap:8px}
.btn-red{position:absolute;background:var(--red);color:var(--white);display:flex;align-items:center;justify-content:center;gap:10px;font-size:22px}

/* about */
.about-title{left:100px;top:672px;font-size:40px;font-weight:400;color:var(--ink)}
.about-tag{left:100px;top:728px;font-size:17px;font-style:italic;color:var(--ink)}
.rule{left:100px;top:775px;width:100px;height:2px;background:var(--ink)}
.para{font-size:12px;line-height:21px;color:#555}
.badge{width:56px;height:56px;border-radius:50%}

/* history */
.history{left:0;top:1143px;width:1200px;height:452px;background:var(--light)}
.history-title{left:606px;width:594px;top:1270px;text-align:center;font-size:42px;font-weight:300;color:var(--ink)}
.history-tag{left:606px;width:594px;top:1330px;text-align:center;font-size:23px;font-style:italic;line-height:37px;color:var(--ink)}
.history-tag em{color:var(--red)}

/* menu */
.section-title{left:0;width:1200px;text-align:center;font-size:40px;font-weight:400;color:var(--ink)}
.dish{position:absolute;width:286px}
.dish-photo{width:286px;height:212px}
.dish-row{display:flex;justify-content:space-between;margin-top:20px;font-size:26px;line-height:37px;color:var(--ink)}
.dish-price{color:var(--red)}

/* connect */
.connect{left:0;top:2588px;width:1200px;height:587px;background:#f9f9f9}
.form-box{left:243px;top:2800px;width:718px;height:300px;border:2px solid var(--red);background:var(--white)}
.field{position:absolute;border-bottom:1px solid #999;font-size:12px;color:#555;padding-bottom:6px}
.contact-panel{left:708px;top:2800px;width:253px;height:300px;background:var(--red);color:var(--white)}

/* map */
.map{left:0;top:3175px;width:1200px;height:278px;background:linear-gradient(135deg,#dfe9d7 0%,#e9eee6 45%,#cfe0c4 100%)}
.map-card{left:653px;top:3279px;width:167px;height:79px;background:var(--red);color:var(--white);padding:12px 14px;font-size:10px;line-height:14px}

/* footer */
.footer{left:0;top:3453px;width:1200px;height:274px;background:var(--footer);color:#ddd}
.f-head{font-size:12px;font-weight:600;color:var(--white);border-bottom:1px solid #aaa;padding-bottom:3px;display:inline-block}
.f-list{list-style:none;font-size:11px;line-height:20px;margin-top:12px;color:#ddd}
</style>
</head>
<body>

<!-- HERO -->
<section class="hero" role="img" aria-label="Plated salmon with fresh salad on a restaurant table">
  <div class="hero-shade"></div>
</section>
<header class="topbar">
  <div class="brand"><div class="brand-name">TEATRO LUCERNA</div><div class="brand-sub">Restaurant &amp; bar</div></div>
  <nav class="nav"><a>Home</a><a>About us</a><a>Reservation</a><a>Latest News</a><a>Contact</a></nav>
  <div class="btn-book">Book Online</div>
</header>
<h1 class="hero-title small">WELCOME TO</h1>
<h1 class="hero-title big">ITALIAN RESTAURANT</h1>
<div class="hero-info" style="top:392px">
  <svg width="22" height="22" viewBox="0 0 24 24" fill="none" stroke="#fff" stroke-width="2"><circle cx="12" cy="12" r="10"/><path d="M12 6v6l4 2"/></svg>
  Opening hours: Mo-Fr 11:00-00:00, &nbsp;Sa-Su 15:00-00:00
</div>
<div class="hero-info" style="top:418px">
  <svg width="16" height="16" viewBox="0 0 24 24" fill="#fff"><path d="M6.6 10.8a15 15 0 006.6 6.6l2.2-2.2c.3-.3.7-.4 1-.2 1.1.4 2.3.6 3.6.6.6 0 1 .4 1 1V20c0 .6-.4 1-1 1A17 17 0 013 4c0-.6.4-1 1-1h3.5c.6 0 1 .4 1 1 0 1.3.2 2.5.6 3.6.1.3 0 .7-.2 1z"/></svg>
  Call (020) 555-0199
</div>
<div class="btn-red" style="left:472px;top:460px;width:226px;height:54px">
  <svg width="26" height="20" viewBox="0 0 26 20" fill="none" stroke="#fff" stroke-width="2"><path d="M2 17h22M4 17a9 9 0 0118 0M13 8V5M10 5h6"/></svg>
  Our Menu
</div>

<!-- ABOUT -->
<h2 class="abs about-title">About Restaurant</h2>
<p class="abs about-tag">The perfect place to enjoy the life and food.</p>
<div class="abs rule"></div>
<p class="abs para" style="left:100px;top:812px;width:400px">It is a long established fact that a reader will be distracted by the readable content of a page when looking at its layout. The point of using Lorem Ipsum is that it has a more-or-less normal distribution of letters, as opposed to using 'Content here'. It is a long established fact that a reader will be distracted by the readable content of a page when looking at its layout.</p>
<div class="abs badge" style="left:104px;top:998px;background:#111"></div>
<div class="abs badge" style="left:204px;top:998px;border:3px solid #222"></div>
<div class="photo" style="left:546px;top:668px;width:268px;height:206px;background:linear-gradient(135deg,#3a2a20,#9a4a25 55%,#2a221c)" role="img" aria-label="Braised meat stew in a cast iron pan"></div>
<div class="photo" style="left:546px;top:879px;width:268px;height:154px;background:linear-gradient(135deg,#4a3a30,#b5673a 50%,#6d7a4a)" role="img" aria-label="Grilled dish with vegetables on a plate"></div>
<div class="photo" style="left:822px;top:668px;width:276px;height:365px;background:linear-gradient(160deg,#cfc6bd,#8a5a3a 50%,#c7b9a8)" role="img" aria-label="Chef garnishing a plated steak"></div>

<!-- HISTORY -->
<section class="abs history"></section>
<div class="photo" style="left:7px;top:1143px;width:599px;height:452px;background:linear-gradient(120deg,#5a5048,#8c7a68 45%,#b53a30 60%,#3c3530)" role="img" aria-label="Smiling waitress in a red apron holding a tablet"></div>
<h2 class="abs history-title">Our History Since 1982</h2>
<p class="abs history-tag">Restaurant is proud to be serving fine Italian<br>dishes for more than <em>30 years!</em></p>
<p class="abs para" style="left:650px;top:1418px;width:506px;text-align:center;font-size:12px;line-height:24px">It is a long established fact that a reader will be distracted by the readable content of a page when looking at its layout. The point of using Lorem Ipsum is that it has a more-or-less normal distribution of letters.</p>

<!-- MENU -->
<h2 class="abs section-title" style="top:1640px">Our Food Menu</h2>
<div class="dish" style="left:124px;top:1746px"><div class="dish-photo" style="background:linear-gradient(135deg,#e8e4de,#d2754a 50%,#7aa04a)" role="img" aria-label="Salmon fillet with green salad"></div><div class="dish-row"><span>Mille-feuille of<br>wild mushrooms</span><span class="dish-price">$4.89</span></div></div>
<div class="dish" style="left:450px;top:1746px"><div class="dish-photo" style="background:linear-gradient(135deg,#3a2620,#8a5a48 50%,#d8cfc8)" role="img" aria-label="Chocolate mousse dessert"></div><div class="dish-row"><span>Mille-feuille of<br>wild mushrooms</span><span class="dish-price">$4.89</span></div></div>
<div class="dish" style="left:778px;top:1746px"><div class="dish-photo" style="background:linear-gradient(135deg,#2a1a15,#6a3a25 50%,#d4a040)" role="img" aria-label="Grilled steak with french fries"></div><div class="dish-row"><span>Mille-feuille of<br>wild mushrooms</span><span class="dish-price">$4.89</span></div></div>
<div class="dish" style="left:124px;top:2084px"><div class="dish-photo" style="background:linear-gradient(135deg,#2a2420,#9a4a25 55%,#3a302a)" role="img" aria-label="Meat stew in a cast iron pan"></div><div class="dish-row"><span>Mille-feuille of<br>wild mushrooms</span><span class="dish-price">$4.89</span></div></div>
<div class="dish" style="left:450px;top:2084px"><div class="dish-photo" style="background:linear-gradient(160deg,#cfc6bd,#8a5a3a 50%,#c79a40)" role="img" aria-label="Chef plating a steak with vegetables"></div><div class="dish-row"><span>Mille-feuille of<br>wild mushrooms</span><span class="dish-price">$4.89</span></div></div>
<div class="dish" style="left:778px;top:2084px"><div class="dish-photo" style="background:linear-gradient(135deg,#7a6a5a,#e8e4de 40%,#d2754a 60%,#6a9a40)" role="img" aria-label="Salmon and salad on a white plate"></div><div class="dish-row"><span>Mille-feuille of<br>wild mushrooms</span><span class="dish-price">$4.89</span></div></div>
<div class="btn-red" style="left:462px;top:2459px;width:263px;height:52px;font-size:21px">
  <svg width="26" height="20" viewBox="0 0 26 20" fill="none" stroke="#fff" stroke-width="2"><path d="M2 17h22M4 17a9 9 0 0118 0M13 8V5M10 5h6"/></svg>
  View All Menu
</div>

<!-- CONNECT -->
<section class="abs connect"></section>
<p class="abs" style="left:0;width:1200px;top:2653px;text-align:center;font-size:14px;color:#666">We are all time available</p>
<h2 class="abs" style="left:0;width:1200px;top:2684px;text-align:center;font-size:34px;font-weight:700;color:var(--ink)">CONNECT WITH US</h2>
<p class="abs" style="left:380px;width:440px;top:2737px;text-align:center;font-size:11px;line-height:19px;color:#555">It is a long established fact that a reader will be distracted by the readable content of a page when looking at its layout.</p>
<div class="abs form-box">
  <div class="abs" style="left:42px;top:30px;font-size:18px;font-weight:600;color:var(--ink)">Send us a Message</div>
  <svg class="abs" style="left:392px;top:30px" width="34" height="28" viewBox="0 0 34 28" fill="none" stroke="#c0201f" stroke-width="2"><rect x="1" y="1" width="32" height="20" rx="2"/><path d="M8 21l-3 6 9-6M7 8h20M7 14h14"/></svg>
  <div class="field" style="left:42px;top:82px;width:176px">Full Name</div>
  <div class="field" style="left:238px;top:82px;width:176px">Ph no</div>
  <div class="field" style="left:42px;top:140px;width:176px">Member<span style="float:right;color:var(--red)">⌄</span></div>
  <div class="field" style="left:238px;top:140px;width:176px">Date Occasion<span style="float:right;color:var(--red)">⌄</span></div>
  <div class="field" style="left:42px;top:200px;width:372px;height:66px">Message</div>
  <div class="abs" style="left:370px;top:200px;width:32px;height:32px;border-radius:50%;background:var(--red)"></div>
  <svg class="abs" style="left:378px;top:208px" width="16" height="16" viewBox="0 0 16 16" fill="#fff"><path d="M1 8l14-7-5 14-2-6z"/></svg>
  <div class="abs" style="left:358px;top:238px;font-size:11px;color:var(--red);font-weight:600">Book Table</div>
</div>
<div class="abs contact-panel">
  <div class="abs" style="left:30px;top:40px;font-size:16px;font-weight:600;border-bottom:1px solid #fff;padding-bottom:6px">Contact Information</div>
  <p class="abs" style="left:30px;top:80px;width:200px;font-size:9px;line-height:13px">It is a long established fact that a reader will be distracted by the readable content.</p>
  <svg class="abs" style="left:30px;top:122px" width="14" height="14" viewBox="0 0 24 24" fill="#fff"><path d="M6.6 10.8a15 15 0 006.6 6.6l2.2-2.2c.3-.3.7-.4 1-.2 1.1.4 2.3.6 3.6.6.6 0 1 .4 1 1V20c0 .6-.4 1-1 1A17 17 0 013 4c0-.6.4-1 1-1h3.5c.6 0 1 .4 1 1 0 1.3.2 2.5.6 3.6.1.3 0 .7-.2 1z"/></svg>
  <div class="abs" style="left:52px;top:120px;font-size:8px">Phone No:</div>
  <div class="abs" style="left:52px;top:131px;font-size:12px;font-weight:600">020-555-0142</div>
  <svg class="abs" style="left:30px;top:160px" width="14" height="11" viewBox="0 0 14 11" fill="none" stroke="#fff"><rect x=".5" y=".5" width="13" height="10"/><path d="M.5 .5l6.5 5 6.5-5"/></svg>
  <div class="abs" style="left:52px;top:156px;font-size:8px">Message:</div>
  <div class="abs" style="left:52px;top:167px;font-size:10px">hello@teatrolucerna.example</div>
  <div class="abs" style="left:48px;top:204px;width:22px;height:22px;border-radius:50%;border:1px solid #fff"></div>
  <div class="abs" style="left:76px;top:204px;width:22px;height:22px;border-radius:50%;border:1px solid #fff"></div>
  <div class="abs" style="left:104px;top:204px;width:22px;height:22px;border-radius:50%;border:1px solid #fff"></div>
</div>

<!-- MAP -->
<div class="abs map" role="img" aria-label="Street map around the restaurant location"></div>
<svg class="abs" style="left:596px;top:3290px" width="36" height="50" viewBox="0 0 36 50"><path d="M18 0a18 18 0 0118 18c0 13-18 32-18 32S0 31 0 18A18 18 0 0118 0z" fill="#222"/><circle cx="18" cy="18" r="7" fill="#fff"/></svg>
<div class="abs map-card"><div style="font-weight:700;text-decoration:underline;margin-bottom:4px">OUR ADDRESS:</div>Lucernastraat 12 –<br>1017 Amsterdam, NL</div>

<!-- FOOTER -->
<footer class="abs footer">
  <div class="abs" style="left:100px;top:48px;width:255px">
    <div class="f-head">ABOUT US</div>
    <p style="font-size:10.5px;line-height:18px;margin-top:12px;text-align:justify">It is a long established fact that a reader will be distracted by the readable content of a page when looking at its layout. It is a long established fact that a reader will be distracted by the readable content of a page.</p>
    <p style="font-size:10.5px;margin-top:14px">Copyright © 2018 website | All Rights Reserved</p>
  </div>
  <div class="abs" style="left:430px;top:48px"><div class="f-head">OUR SERVICE</div><ul class="f-list"><li>Food item</li><li>Food item</li><li>Food item</li><li>Food item</li><li>Food item</li><li>Food item</li><li>Food item</li></ul></div>
  <div class="abs" style="left:604px;top:48px"><div class="f-head">SITELINK</div><ul class="f-list"><li>Home</li><li>About us</li><li>Reservation</li><li>Latest news</li><li>Contact us</li><li>Book online</li></ul></div>
  <div class="abs" style="left:777px;top:48px"><div class="f-head">OUR SPECIALITY</div><ul class="f-list"><li>Affordable price</li><li>Quality service</li><li>Supior quality</li></ul></div>
  <div class="abs" style="left:961px;top:48px"><div class="f-head">COMPANY RULES</div><ul class="f-list"><li>Rules &amp; Regulation</li><li>Terms &amp; Conditions</li><li>Privacy Policy</li><li>Help</li></ul></div>
</footer>

</body>
</html>
```